Business Card Design

I need a business card for a new company based in Australia called "MedLinkora".

Its a cloud program for GPs that allows them to search for the specialist they require using a simple user friendly tool.

I would like the colours to match those in the program (the colours in the logo attached).

The final design should reflect the programs clarity, ease of use and professionalism.

Target Market(s)

GPs and other Health Professionals

Industry/Entity Type

Business

Contact Information for Business Card

MedLinkora; The Trusted Clinician Index; Marla Ostrove CEO; 0438215906; marla@medlinkora.example; www.medlinkora.example

Requirements
Must have
• Must have the logo attached; the web address and my name and phone number
Nice to have
• the slogan "The Trusted Clinician Index"

```html
<!DOCTYPE html>
<html lang="en">
<head>
<meta charset="utf-8">
<title>MedLinkora Business Card</title>
<link href="https://fonts.googleapis.com/css2?family=Open+Sans:wght@300;400;600;700&display=swap" rel="stylesheet">
<style>
  :root {
    --page: #e9eaec;
    --card-grey: #4f5052;
    --panel-grey: #444547;
    --brand-blue: #10aee2;
    --band-blue: #0cb0e0;
    --ink-dark: #2b2c2e;
    --slogan-grey: #8c8d8f;
    --white: #ffffff;
  }
  * { box-sizing: border-box; margin: 0; padding: 0; }
  html, body { width: 1200px; height: 800px; overflow: hidden; }
  body {
    background: var(--page);
    font-family: "Open Sans", Arial, sans-serif;
    display: flex;
    align-items: center;
    justify-content: center;
    gap: 40px;
  }
  .card {
    position: relative;
    width: 560px;
    height: 320px;
    background: var(--card-grey);
    overflow: hidden;
    box-shadow: 0 6px 18px rgba(0,0,0,0.18);
  }
  /* Front */
  .front-logo {
    position: absolute;
    left: 0; right: 0; top: 112px;
    text-align: center;
  }
  .front-logo .wordmark {
    color: var(--brand-blue);
    font-size: 66px;
    font-weight: 400;
    letter-spacing: -1px;
    line-height: 1;
  }
  .front-logo .slogan {
    color: var(--slogan-grey);
    font-size: 22px;
    font-weight: 300;
    letter-spacing: 1px;
    margin-top: 4px;
  }
  /* Back */
  .band {
    position: absolute;
    left: 0; top: 0;
    width: 100%; height: 118px;
    background: var(--band-blue);
  }
  .band-name {
    position: absolute;
    right: 26px; top: 30px;
    text-align: right;
  }
  .band-name .wordmark {
    color: var(--ink-dark);
    font-size: 40px;
    font-weight: 600;
    line-height: 1;
    letter-spacing: -0.5px;
  }
  .band-name .slogan {
    color: var(--white);
    font-size: 13px;
    font-weight: 400;
    margin-top: 4px;
  }
  .logo-panel {
    position: absolute;
    left: 30px; top: 136px;
    width: 240px; height: 166px;
    background: var(--panel-grey);
    display: flex;
    flex-direction: column;
    justify-content: center;
    align-items: center;
  }
  .logo-panel .wordmark {
    color: var(--brand-blue);
    font-size: 34px;
    font-weight: 400;
    letter-spacing: -0.5px;
    line-height: 1;
  }
  .logo-panel .slogan {
    color: var(--slogan-grey);
    font-size: 11.5px;
    font-weight: 300;
    margin-top: 4px;
  }
  .contact {
    position: absolute;
    left: 290px; top: 140px;
    width: 240px;
  }
  .contact .person {
    color: var(--brand-blue);
    font-size: 19px;
    font-weight: 400;
    line-height: 1.1;
  }
  .contact .person strong { font-weight: 700; }
  .contact .role {
    color: var(--white);
    font-size: 13px;
    font-weight: 400;
  }
  .rule {
    height: 1px;
    background: var(--brand-blue);
    margin: 8px 0 10px;
  }
  .contact ul { list-style: none; }
  .contact li {
    display: flex;
    align-items: center;
    gap: 10px;
    color: var(--white);
    font-size: 13.5px;
    line-height: 1.65;
  }
  .contact li svg { width: 12px; height: 12px; flex: none; }
  .contact .rule.bottom { margin-top: 14px; }
</style>
</head>
<body>
  <section class="card card-front" aria-label="Card front">
    <div class="front-logo">
      <div class="wordmark">MedLinkora</div>
      <div class="slogan">The Trusted Clinician Index</div>
    </div>
  </section>

  <section class="card card-back" aria-label="Card back">
    <div class="band">
      <div class="band-name">
        <div class="wordmark">MedLinkora</div>
        <div class="slogan">The Trusted Clinician Index</div>
      </div>
    </div>

    <div class="logo-panel">
      <div class="wordmark">MedLinkora</div>
      <div class="slogan">The Trusted Clinician Index</div>
    </div>

    <div class="contact">
      <div class="person"><strong>MARLA</strong> OSTROVE</div>
      <div class="role">CEO</div>
      <div class="rule"></div>
      <ul>
        <li>
          <svg viewBox="0 0 12 12" aria-hidden="true"><path fill="#fff" d="M1 4c0-2 2-3 5-3s5 1 5 3v1H8.5V3.8h-5V5H1zM2.5 6h7l1 5h-9z"/><circle cx="6" cy="8.3" r="1.2" fill="#4f5052"/></svg>
          0438215906
        </li>
        <li>
          <svg viewBox="0 0 12 12" aria-hidden="true"><rect x="0.5" y="2" width="11" height="8" fill="#fff"/><path d="M0.5 2 6 6.8 11.5 2" fill="none" stroke="#4f5052" stroke-width="1"/></svg>
          marla@medlinkora.example
        </li>
        <li>
          <svg viewBox="0 0 12 12" aria-hidden="true"><g fill="none" stroke="#fff" stroke-width="1"><circle cx="6" cy="6" r="5"/><ellipse cx="6" cy="6" rx="2.2" ry="5"/><path d="M1 6h10M2 3.5h8M2 8.5h8"/></g></svg>
          www.medlinkora.example
        </li>
      </ul>
      <div class="rule bottom"></div>
    </div>
  </section>
</body>
</html>
```